MOLVT Study flyer

I need help designing a flyer for a research study that will include brain imaging in adolescents. The info is in the attached document. The study is called the Marrowby Orchard Lantern Vesper Trail (MOLVT) study. Ideally this would be returned as a document that I can edit in the future as we will have several new recruitment phases (different age groups, etc. I also would love to have a logo designed as part of this project, but I recognize that might be a separate design request.

```html
<!DOCTYPE html>
<html lang="en">
<head>
<meta charset="utf-8">
<title>MOLVT Study Flyer</title>
<link rel="stylesheet" href="https://fonts.googleapis.com/css2?family=Arimo:wght@400;700&family=Open+Sans:wght@700;800&display=swap">
<style>
  :root {
    --brand-blue: #1a66ee;
    --deep-blue: #0a2df0;
    --ring-blue: #6fd3ff;
    --panel-grey: #dcdde2;
    --ink: #0a0a0a;
    --white: #ffffff;
  }
  * { margin: 0; padding: 0; box-sizing: border-box; }
  html, body { width: 927px; height: 1200px; overflow: hidden; background: var(--white); }
  .flyer {
    position: relative;
    width: 927px;
    height: 1200px;
    overflow: hidden;
    font-family: "Arimo", Arial, sans-serif;
    color: var(--ink);
    background: linear-gradient(90deg, var(--white) 60%, #eef2fd 100%);
  }
  .backdrop { position: absolute; inset: 0; }
  .brand {
    position: absolute;
    left: 47px; top: 42px;
    display: flex; align-items: center; gap: 30px;
  }
  .brand-mark {
    width: 110px; height: 110px;
    border: 5px solid var(--brand-blue);
    border-radius: 50%;
  }
  .brand-name {
    font-weight: 700;
    font-size: 92px;
    line-height: 1;
    color: var(--brand-blue);
    letter-spacing: 1px;
  }
  .intro-question {
    position: absolute;
    left: 0; width: 560px; top: 192px;
    text-align: center;
    font-weight: 700; font-size: 25px; line-height: 30px;
    white-space: nowrap;
  }
  .study-summary {
    position: absolute;
    left: 24px; top: 314px;
    font-weight: 700; font-size: 22.5px; line-height: 30px;
    letter-spacing: 0.4px;
    white-space: nowrap;
  }
  .involves {
    font-family: "Open Sans", Verdana, sans-serif;
    font-weight: 800;
    font-size: 23px;
    letter-spacing: 0.6px;
  }
  .involves-title {
    position: absolute;
    left: 20px; width: 520px; top: 498px;
    text-align: center; line-height: 32px;
  }
  .involves-item {
    position: absolute;
    left: 20px; width: 520px;
    text-align: center; line-height: 37.5px;
    white-space: nowrap;
  }
  .item-interview { top: 536px; }
  .item-questionnaires { top: 648px; }
  .item-visit { top: 722px; }
  .bullet {
    position: absolute;
    left: 26px;
    width: 31px; height: 31px;
    border-radius: 50%;
    background: var(--brand-blue);
    border: 4px solid var(--ring-blue);
  }
  .compensation {
    position: absolute;
    left: 48px; top: 938px;
    font-size: 38px; line-height: 44px;
  }
  .compensation-amount {
    position: absolute;
    left: 47px; top: 984px;
    font-weight: 700; font-size: 60px; line-height: 66px;
    color: var(--deep-blue);
    transform: scaleX(0.9); transform-origin: left center;
  }
  .eligibility {
    position: absolute;
    left: 558px; width: 369px; top: 107px;
    text-align: center;
    white-space: nowrap;
  }
  .eligibility-title {
    font-weight: 700; font-size: 37.5px; line-height: 37px;
    letter-spacing: 0.3px;
  }
  .eligibility-item {
    position: absolute; left: 0; width: 100%;
    font-weight: 700; font-size: 26.5px; line-height: 29px;
  }
  .crit-age { top: 103px; }
  .crit-worry { top: 161px; }
  .crit-diagnosis { top: 248px; }
  .crit-contact { top: 363px; }
  .contact-email {
    position: absolute;
    left: 612px; top: 772px;
    font-weight: 700; font-size: 21px; line-height: 26px;
    color: var(--brand-blue);
    transform: rotate(-33deg); transform-origin: left center;
    white-space: nowrap;
  }
  .brain-artwork { position: absolute; left: 545px; top: 866px; }
</style>
</head>
<body>
<main class="flyer">
  <svg class="backdrop" width="927" height="1200" viewBox="0 0 927 1200" aria-hidden="true">
    <defs>
      <linearGradient id="headerSky" x1="0" y1="0" x2="0" y2="1">
        <stop offset="0" stop-color="#ffffff"/>
        <stop offset="1" stop-color="#c9d8fb"/>
      </linearGradient>
      <linearGradient id="bandFade" x1="1" y1="0" x2="0" y2="1">
        <stop offset="0" stop-color="#1a66ee"/>
        <stop offset="0.55" stop-color="#7ea3f6"/>
        <stop offset="1" stop-color="#ffffff" stop-opacity="0"/>
      </linearGradient>
      <linearGradient id="cornerGrey" x1="0" y1="1" x2="1" y2="0">
        <stop offset="0" stop-color="#ffffff"/>
        <stop offset="0.6" stop-color="#dedfe6"/>
        <stop offset="1" stop-color="#a9acb8"/>
      </linearGradient>
      <linearGradient id="panelFade" x1="0" y1="0" x2="1" y2="1">
        <stop offset="0.55" stop-color="#dcdde2"/>
        <stop offset="1" stop-color="#ffffff"/>
      </linearGradient>
    </defs>
    <rect class="header-band" x="0" y="0" width="560" height="180" fill="url(#headerSky)"/>
    <path class="info-panel" d="M0 178 H540 Q547 178 547 185 V1200 H0 Z" fill="var(--panel-grey)"/>
    <polygon class="panel-sweep" points="0,1200 547,890 547,1200" fill="url(#panelFade)"/>
    <polygon class="corner-field" points="110,1200 927,680 927,1200" fill="url(#cornerGrey)"/>
    <polygon class="accent-band" points="927,625 927,680 110,1200 40,1200" fill="url(#bandFade)"/>
    <polygon class="accent-band-lower" points="927,1075 927,1120 760,1200 700,1200" fill="var(--brand-blue)"/>
  </svg>

  <header class="brand">
    <span class="brand-mark"></span>
    <span class="brand-name">MOLVT</span>
  </header>

  <p class="intro-question">Are you the parent of a child age 10-17?<br>Do they worry or overthink negative<br>emotions?</p>

  <p class="study-summary">Harlow Ridge University researchers are<br>seeking girls age 10-17 for a study about<br>brain activity in emotions and deci-<br>sion-making and how they relate to<br>puberty, anxiety and depression.</p>

  <section class="involves">
    <h2 class="involves-title involves">Study participation involves:</h2>
    <span class="bullet" style="top:540px"></span>
    <p class="involves-item item-interview">&nbsp;&nbsp;&nbsp;One one-hour interview (online or<br>in-person) where your child will<br>discuss their thoughts</p>
    <span class="bullet" style="top:651px"></span>
    <p class="involves-item item-questionnaires">&nbsp;&nbsp;&nbsp;Online questionnaires (parent and<br>child)</p>
    <span class="bullet" style="top:725px"></span>
    <p class="involves-item item-visit">&nbsp;&nbsp;&nbsp;One two-hour visit where your<br>child will complete an MRI scan,<br>answer questions about their puberty<br>stage, and have a small hair sample<br>taken to study puberty hormones</p>
  </section>

  <p class="compensation">Compensation up to</p>
  <p class="compensation-amount">$140</p>

  <section class="eligibility">
    <h2 class="eligibility-title">Your child may be<br>eligible if they:</h2>
    <p class="eligibility-item crit-age">Are age 10-17</p>
    <p class="eligibility-item crit-worry">Tend to worry or overthink<br>negative thoughts</p>
    <p class="eligibility-item crit-diagnosis">have not been diagnosed<br>with psychosis, learning<br>problems, or autism</p>
    <p class="eligibility-item crit-contact">Interested in participating?<br>Want more information?<br>Please contact us!</p>
  </section>

  <p class="contact-email">molvtstudy@harlowridge.edu</p>

  <svg class="brain-artwork" width="382" height="334" viewBox="0 0 382 334" role="img" aria-label="Illustration of a glowing blue brain inside a dark human head silhouette">
    <defs>
      <radialGradient id="brainGlow" cx="0.45" cy="0.4" r="0.6">
        <stop offset="0" stop-color="#3aa6e8"/>
        <stop offset="0.55" stop-color="#1d5d9a"/>
        <stop offset="1" stop-color="#0b0b0b"/>
      </radialGradient>
    </defs>
    <path d="M60 334 C10 290 0 200 40 130 C80 55 170 10 260 20 C330 28 382 70 382 90 V334 Z" fill="url(#brainGlow)"/>
  </svg>
</main>
</body>
</html>
```